Velmora Water Purification

We need a website set up on a "Free account" WordPress platform. (This is the type of Wordpress site that you can sign up for and create online for free (not a server-hosted type.)
The website will be for a water purification company. They install devices in homes to purify the water for safer drinking, bathing, and cleaning.
Our logo is attached. Please keep color scheme of the website consistent with the logo.
Water Purification

```html
<!DOCTYPE html>
<html lang="en">
<head>
<meta charset="utf-8">
<title>Velmora Water Purification</title>
<link rel="stylesheet" href="https://fonts.googleapis.com/css2?family=Kaushan+Script&family=Lato:wght@400;700&display=swap">
<style>
:root{
  --navy:#121a55;
  --navy-deep:#0d1440;
  --blue:#1d8fc8;
  --blue-dark:#146d9c;
  --slate:#6b6f79;
  --slate-light:#7a7e88;
  --text:#5a5a5a;
  --paper:#ffffff;
  --mist:#f4f4f4;
  --line:#d6d6d6;
}
*{box-sizing:border-box;margin:0;padding:0}
html,body{width:1200px;height:2826px;overflow:hidden}
body{position:relative;background:var(--paper);font-family:'Lato',sans-serif;color:var(--text)}
.abs{position:absolute}
.script{font-family:'Kaushan Script',cursive;color:var(--navy)}
.btn{position:absolute;display:flex;align-items:center;justify-content:center;border-radius:24px;font-size:19px;letter-spacing:.5px;box-shadow:0 4px 0 rgba(0,0,0,.18)}
.btn-white{background:var(--paper);color:#222}
.btn-blue{background:var(--blue);color:#fff;box-shadow:0 4px 0 var(--blue-dark)}

/* hero */
.hero{left:0;top:0;width:1200px;height:635px;background:linear-gradient(100deg,#8e9094 0%,#c9cacc 30%,#a9a7a2 60%,#5d5a55 100%)}
.brand{left:75px;top:40px;display:flex;align-items:center;gap:14px}
.brand-dot{width:46px;height:46px;border-radius:50%;background:var(--blue)}
.brand-name{font-family:'Lato',sans-serif;font-weight:700;font-size:30px;color:var(--navy)}
.nav{left:475px;top:53px;display:flex;gap:0}
.nav a{display:flex;align-items:center;height:37px;font-size:14px;color:#111;text-decoration:none;padding:0 0;position:absolute;white-space:nowrap}
.nav .active{background:var(--blue);color:#fff;border-radius:18px;width:90px;justify-content:center}
.hero-title{right:75px;top:192px;font-size:56px;color:#fff;white-space:nowrap}
.hero-title small{font-size:36px}
.hero-sub{right:75px;top:281px;font-size:26px;color:#fff}
.hero-copy{right:84px;top:327px;width:570px;font-size:13.5px;line-height:22px;color:#3a3a3a;text-align:center}

/* about */
.heading{font-family:'Kaushan Script',cursive;color:var(--navy);font-size:54px;text-align:center;width:1200px;left:0}
.body-copy{font-size:14.5px;line-height:22px;text-align:center}

/* service */
.service-panel{left:0;top:993px;width:601px;height:467px;background:var(--slate)}
.service-photo{left:601px;top:993px;width:599px;height:467px;background:linear-gradient(120deg,#e9ecef 0%,#cfd3d6 45%,#8f8580 75%,#d9dcde 100%)}

/* news */
.news{left:0;top:1978px;width:1200px;height:566px;background:var(--mist)}
.card{position:absolute;top:2125px;width:300px;height:281px;background:var(--paper)}
.card .photo{width:300px;height:164px}
.card h3{font-family:'Kaushan Script',cursive;font-weight:400;color:#1a1a1a;font-size:24px;text-align:center;margin-top:22px}
.card p{font-size:14px;line-height:20px;text-align:center;width:170px;margin:8px auto 0}
.pager{position:absolute;top:2449px;width:40px;height:42px;border:1px solid #bbb;background:#fff;display:flex;align-items:center;justify-content:center}

/* footer */
.footer{left:0;top:2544px;width:1200px;height:229px;background:var(--slate-light)}
.footer h4{font-family:'Kaushan Script',cursive;font-weight:400;color:var(--navy);font-size:22px}
.footer .item{display:flex;gap:14px;font-size:14px;line-height:20px;color:#fff;align-items:flex-start}
.legal{left:0;top:2773px;width:1200px;height:53px;background:var(--navy-deep)}
.social{width:20px;height:20px;border-radius:50%;background:#e7e8ee}
</style>
</head>
<body>

<!-- hero -->
<section class="abs hero" role="img" aria-label="Chrome kitchen tap pouring water into a white sink"></section>
<div class="abs brand"><span class="brand-dot"></span><span class="brand-name">Velmora</span></div>
<nav class="abs nav" style="width:650px;height:37px">
  <a class="active" style="left:0">HOME</a>
  <a style="left:118px">ABOUT</a>
  <a style="left:216px">SERVICE</a>
  <a style="left:322px">TESTIMONIAL</a>
  <a style="left:465px">NEWS</a>
  <a style="left:557px">CONTACT US</a>
</nav>
<h1 class="abs hero-title script" style="font-weight:400">Velmora <small>Water Purification</small></h1>
<p class="abs hero-sub">Great tasting, Clean Water Straight From Your Tap.</p>
<p class="abs hero-copy">Lorem Ipsum is simply dummy text of the printing and typesetting industry. Lorem Ipsum has been the industry's standard dummy text ever since the 1500.</p>
<a class="btn btn-white" style="left:880px;top:386px;width:239px;height:47px">CONTACT US NOW</a>

<!-- about -->
<h2 class="abs heading" style="top:680px;font-weight:400">About Velmora</h2>
<p class="abs body-copy" style="left:122px;top:774px;width:956px">Lorem Ipsum is simply dummy text of the printing and typesetting industry. Lorem Ipsum has been the industry's standard dummy text ever since the 1500s, when an unknown printer took a galley of type and scrambled it to make a type specimen book. It has survived not only five centuries, but also the leap into electronic typesetting, remaining essentially unchanged. It was popularised in the 1960s with the release of Letraset sheets containing Lorem Ipsum passages.</p>
<a class="btn btn-blue" style="left:511px;top:880px;width:177px;height:47px">READ MORE</a>

<!-- service -->
<section class="abs service-panel"></section>
<h2 class="abs script" style="left:0;top:1065px;width:601px;text-align:center;font-size:54px;font-weight:400">Service</h2>
<p class="abs script" style="left:0;top:1146px;width:601px;text-align:center;font-size:23px;color:#fff">Install Devices in homes to purify the water</p>
<p class="abs body-copy" style="left:41px;top:1192px;width:520px;color:#e3e4e8">Lorem Ipsum is simply dummy text of the printing and typesetting industry. Lorem Ipsum has been the industry's standard dummy text ever since the 1500s, when an unknown printer took a galley of type and scrambled it to make a type specimen book. It has survived not only five centuries, but also the leap into electronic typesetting, remaining essentially unchanged. It was popularised in the 1960s with the release of Letraset sheets containing.</p>
<a class="btn btn-white" style="left:205px;top:1336px;width:177px;height:45px">READ MORE</a>
<section class="abs service-photo" role="img" aria-label="Woman filling a glass with filtered water at a kitchen tap"></section>

<!-- testimonial -->
<h2 class="abs heading" style="top:1508px;font-weight:400">Testimonial</h2>
<svg class="abs" style="left:0;top:1594px" width="640" height="66" viewBox="0 0 640 66">
  <line x1="0" y1="32" x2="567" y2="32" stroke="var(--blue)" stroke-width="2" stroke-dasharray="5 4"/>
  <circle cx="599" cy="32" r="32" fill="var(--blue)"/>
  <path d="M585 38a6 6 0 1 0 6-6c0-4 2-7 6-8v-3c-7 1-12 7-12 14zm16 0a6 6 0 1 0 6-6c0-4 2-7 6-8v-3c-7 1-12 7-12 14z" fill="#fff"/>
</svg>
<p class="abs body-copy" style="left:203px;top:1692px;width:795px">Lorem Ipsum is simply dummy text of the printing and typesetting industry. Lorem Ipsum has been the industry's standard dummy text ever since the 1500s, when an unknown printer took a galley of type and scrambled it to make a type specimen book. It has survived not only five centuries.</p>
<div class="abs" style="left:548px;top:1782px;width:102px;height:102px;border-radius:50%;border:2px solid var(--navy);padding:5px"><div role="img" aria-label="Client portrait" style="width:100%;height:100%;border-radius:50%;background:linear-gradient(160deg,#d8d4d0,#9a7d6a)"></div></div>
<p class="abs" style="left:675px;top:1820px;font-size:20px;color:var(--navy)">Lorem ipsum</p>
<div class="abs" style="left:528px;top:1923px;width:38px;height:4px;background:var(--navy)"></div>
<div class="abs" style="left:578px;top:1923px;width:42px;height:4px;background:var(--blue)"></div>
<div class="abs" style="left:629px;top:1923px;width:42px;height:4px;background:var(--navy)"></div>

<!-- news -->
<section class="abs news"></section>
<h2 class="abs heading" style="top:2030px;font-weight:400">Latest News</h2>
<article class="card" style="left:0;border-bottom:3px solid var(--slate)"><div class="photo" role="img" aria-label="Family shopping for water filters" style="background:linear-gradient(135deg,#6d8fb8,#2f5fa0)"></div><h3>Lorem ipsum dummy text</h3><p>Lorem Ipsum is simply dummy text of the printing.</p></article>
<svg class="abs" style="left:98px;top:2185px" width="110" height="44" viewBox="0 0 110 44">
  <circle cx="22" cy="22" r="22" fill="#555b66"/><circle cx="20" cy="20" r="7" fill="none" stroke="#fff" stroke-width="2.5"/><line x1="25" y1="25" x2="31" y2="31" stroke="#fff" stroke-width="3"/>
  <circle cx="82" cy="22" r="22" fill="var(--navy)"/><path d="M76 28l12-12M74 22l-3 3a4 4 0 0 0 6 6l3-3M90 22l3-3a4 4 0 0 0-6-6l-3 3" stroke="#fff" stroke-width="2.5" fill="none"/>
</svg>
<article class="card" style="left:300px"><div class="photo" role="img" aria-label="Woman drinking a glass of water outdoors" style="background:linear-gradient(135deg,#cfd8c8,#8f9a80)"></div><h3>Lorem ipsum dummy text</h3><p>Lorem Ipsum is simply dummy text of the printing.</p></article>
<article class="card" style="left:600px"><div class="photo" role="img" aria-label="Water poured into a glass on a blue surface" style="background:linear-gradient(180deg,#6e97bd,#1f4f7e)"></div><h3>Lorem ipsum dummy text</h3><p>Lorem Ipsum is simply dummy text of the printing.</p></article>
<article class="card" style="left:900px"><div class="photo" role="img" aria-label="Modern chrome bathroom faucet" style="background:linear-gradient(135deg,#eceef0,#9ea3a8)"></div><h3>Lorem ipsum dummy text</h3><p>Lorem Ipsum is simply dummy text of the printing.</p></article>
<div class="pager" style="left:454px"><svg width="10" height="14"><path d="M8 1L2 7l6 6" stroke="#777" fill="none"/></svg></div>
<a class="btn btn-white" style="left:511px;top:2449px;width:177px;height:42px;border:1px solid #ccc">VIEW ALL</a>
<div class="pager" style="left:703px"><svg width="10" height="14"><path d="M2 1l6 6-6 6" stroke="#777" fill="none"/></svg></div>

<!-- footer -->
<footer class="abs footer">
  <div class="abs" style="left:120px;top:60px;width:230px;display:flex;align-items:center;gap:12px;justify-content:center"><span class="brand-dot"></span><span class="brand-name">Velmora</span></div>
  <p class="abs" style="left:82px;top:164px;width:310px;text-align:center;font-size:14px;line-height:20px;color:#fff">Lorem Ipsum has been the industry's standard dummy text ever since the 1500.</p>

  <h4 class="abs" style="left:435px;top:42px">Contact Info</h4>
  <div class="abs item" style="left:435px;top:92px;width:300px"><svg width="22" height="20" viewBox="0 0 22 20"><path d="M1 4l6-3 8 3 6-3v15l-6 3-8-3-6 3z M7 1v15 M15 4v15" stroke="#fff" fill="none" stroke-width="1.5"/></svg><span>123 Building Name, Street Name, City, Country - Zipcode</span></div>
  <div class="abs item" style="left:435px;top:142px"><svg width="22" height="20" viewBox="0 0 22 20"><path d="M4 2h4l2 5-3 2a11 11 0 0 0 5 5l2-3 5 2v4a2 2 0 0 1-2 2A17 17 0 0 1 2 4a2 2 0 0 1 2-2z" stroke="#fff" fill="none" stroke-width="1.5"/></svg><span>123 456 7878</span></div>
  <div class="abs item" style="left:435px;top:176px"><svg width="22" height="20" viewBox="0 0 22 20"><rect x="1" y="3" width="20" height="14" stroke="#fff" fill="none" stroke-width="1.5"/><path d="M1 3l10 8 10-8" stroke="#fff" fill="none" stroke-width="1.5"/></svg><span>info@velmorawater.com</span></div>

  <h4 class="abs" style="left:791px;top:42px">Subscribe</h4>
  <p class="abs" style="left:791px;top:88px;width:330px;font-size:14px;line-height:22px;color:#fff">Sign up to get updates about news &amp; Events of Northfield Harbor House Inc.</p>
  <div class="abs" style="left:789px;top:135px;width:334px;height:55px;background:#fff;border-radius:28px 0 0 28px;display:flex;align-items:center;padding-left:24px;font-size:13px;font-style:italic;color:#888">Enter E-Mail Address</div>
  <div class="abs" style="left:1027px;top:135px;width:96px;height:55px;background:var(--blue);border-radius:0 28px 28px 0;display:flex;align-items:center;justify-content:center;color:#fff;font-weight:700;font-size:17px">SIGN UP</div>
</footer>
<section class="abs legal">
  <p class="abs" style="left:85px;top:17px;font-size:14px;color:#6b7096;white-space:nowrap">© <span class="script" style="color:#fff;font-size:16px">Velmora water purification</span> 2017, All Rights Reserved</p>
  <div class="abs" style="left:1008px;top:17px;display:flex;gap:22px"><span class="social"></span><span class="social"></span><span class="social"></span><span class="social"></span></div>
</section>

</body>
</html>
```